Acupuncture Medspa needs a business card design

I need a business card design that looks professional, has a spa-like quality and can offer a promo on the back. Initial promo is "First session free". The tagline of NeedleNook is: Refresh, Restore, Rejuvenate.

NeedleNook is a membership-based acupuncture medspa that offers acupuncture, cupping, and herbal therapies. Members choose between the "Refresh" membership which is for stress relief, or "Restore" which is for treating health conditions, and lastly "Rejuvenate" which is for natural facial enhancement.

Industry/Entity Type

Health And Wellness

Contact Information for Business Card

Coral Haskins, MAC, L.Ac.
612-555-0193
www.needlenook-example.com

Font styles to use
Serif
Sans Serif

Colors

Designer to choose colors to be used in the design.

Requirements
Must have
• The project must have NeedleNook logo, promo on the back, and contact information
Nice to have
• I would like to see the colors of the logo used.

```html
<!DOCTYPE html>
<html lang="en">
<head>
<meta charset="UTF-8">
<title>NeedleNook Business Card</title>
<link rel="stylesheet" href="https://fonts.googleapis.com/css2?family=Poppins:wght@400;500&family=Cormorant+Garamond:ital,wght@1,500&display=swap">
<style>
  :root {
    --teal: #3a8780;
    --brown: #4a2c13;
    --brown-deep: #41230e;
    --ink: #555555;
    --rule: #9a9a9a;
    --paper: #ffffff;
    --backdrop: #e6e6e6;
  }
  * { margin: 0; padding: 0; box-sizing: border-box; }
  html, body { width: 1200px; height: 1200px; overflow: hidden; }
  body {
    background: var(--backdrop);
    font-family: "Poppins", sans-serif;
    position: relative;
  }
  .card {
    position: absolute;
    left: 200px;
    width: 800px;
    height: 457px;
    overflow: hidden;
  }
  .card-front { top: 88px; background: var(--paper); }
  .card-back {
    top: 655px;
    background: linear-gradient(180deg, var(--brown) 0%, var(--brown-deep) 100%);
  }

  .brand-name {
    position: absolute;
    right: 50px;
    top: 70px;
    display: flex;
    align-items: center;
    gap: 12px;
    font-weight: 500;
    font-size: 44px;
    letter-spacing: 1px;
    color: var(--teal);
    line-height: 1;
  }
  .brand-dot {
    width: 16px; height: 16px;
    border-radius: 50%;
    background: var(--teal);
  }

  .holder {
    position: absolute;
    left: 50px;
    top: 304px;
    color: var(--teal);
    font-weight: 500;
    font-size: 31px;
    line-height: 1;
  }
  .holder .credentials { font-size: 17px; margin-left: 2px; }
  .divider {
    position: absolute;
    left: 50px; right: 50px;
    top: 353px;
    height: 2px;
    background: var(--rule);
  }
  .contact {
    position: absolute;
    left: 50px;
    top: 368px;
    list-style: none;
    color: var(--ink);
    font-size: 19px;
    line-height: 25px;
  }
  .contact li { display: flex; align-items: center; gap: 8px; }
  .contact svg { width: 18px; height: 18px; fill: var(--teal); flex: none; }

  .accent-band {
    position: absolute;
    left: 0; bottom: 0;
    width: 800px; height: 16px;
  }

  .promo {
    position: absolute;
    left: 0; right: 0;
    top: 190px;
    text-align: center;
    font-family: "Cormorant Garamond", serif;
    font-style: italic;
    font-weight: 500;
    font-size: 92px;
    color: var(--teal);
    line-height: 1;
  }
  .tagline {
    position: absolute;
    left: 0; right: 0;
    top: 388px;
    text-align: center;
    color: #ffffff;
    font-size: 19px;
  }
  .tagline .sep { color: var(--teal); margin: 0 4px; }
</style>
</head>
<body>
  <section class="card card-front">
    <div class="brand-name"><span class="brand-dot"></span>NEEDLENOOK</div>
    <h1 class="holder">Coral Haskins, <span class="credentials">MAC, L.Ac.</span></h1>
    <div class="divider"></div>
    <ul class="contact">
      <li>
        <svg viewBox="0 0 24 24" aria-hidden="true"><path d="M6.6 10.8a15.1 15.1 0 0 0 6.6 6.6l2.2-2.2c.3-.3.7-.4 1-.2 1.1.4 2.3.6 3.6.6.6 0 1 .4 1 1V20c0 .6-.4 1-1 1A17 17 0 0 1 3 4c0-.6.4-1 1-1h3.5c.6 0 1 .4 1 1 0 1.3.2 2.5.6 3.6.1.3 0 .7-.2 1z"/></svg>
        612-555-0193
      </li>
      <li>
        <svg viewBox="0 0 24 24" aria-hidden="true"><path d="M12 2a10 10 0 1 0 0 20 10 10 0 0 0 0-20zm-1 17.9A8 8 0 0 1 4.1 11L9 16v1c0 1.1.9 2 2 2zm6.9-2.5A2 2 0 0 0 16 16h-1v-3c0-.6-.4-1-1-1H8v-2h2c.6 0 1-.4 1-1V7h2c1.1 0 2-.9 2-2v-.4a8 8 0 0 1 2.9 12.8z"/></svg>
        www.needlenook-example.com
      </li>
    </ul>
    <svg class="accent-band" viewBox="0 0 800 16" preserveAspectRatio="none" aria-hidden="true">
      <polygon points="0,0 524,0 519,16 0,16" fill="var(--teal)"/>
      <polygon points="528,0 800,0 800,16 523,16" fill="var(--brown)"/>
    </svg>
  </section>

  <section class="card card-back">
    <p class="promo">first session free.</p>
    <p class="tagline">Refresh<span class="sep">•</span>Restore<span class="sep">•</span>Rejuvenate.</p>
  </section>
</body>
</html>
```